Buch-/E-Book-Cover für einen Eltern-Ratgeber
Zielgruppe
Ich bin Autor/Self-Publisher von Büchern/E-Books.
Aufgabenstellung
Ich benötige ein Buchcover (Print Paperback und E-Book) für einen kurzen Eltern-Ratgeber (ca. 60 Seiten):
Titel: 'Kleine Helden im Badezimmer'
Autorin: Frieda Wolkenstein
FW Verlag, Berlin
Das Buch richtet sich an verzweifelte Eltern und gibt Tipps, wie sie ihre kleinen Kinder zum Zähne putzen animieren können. Für die Gestaltung gerne vorzugsweise Fotos von echten Menschen (Eltern + Kind bzw. nur Kind bzw. 2 Kinder). Illustrierte Cover sind auch OK, aber nicht präferiert. Für Vorschläge bitte *inklusive Rückseite* und an bestehenden Eltern-Ratgebern orientieren, die Buchhafen zu finden sind, wie zum Beispiel:
- Wiegenzeit von Tilo K. Brenner
- PAPA im Takt von Nora Fendt
- Mutig durch den Alltag von Wiebke Tolan
- Grenzen setzen ohne Streit von Gudrun Vell-Borm
Auf den Buchseiten sind Illustrationen enthalten, die mit dem Buchcover möglichst auch harmonisieren sollten. Die Entwürfe der Illustrationen sind hier hochgeladen.
Ggf. kann man mit einer Text-Banderole/Kreis arbeiten, mit der Aufschrift '21 praktische Tipps für Eltern'
Klappentext:
Ihr Kind will sich partout nicht die Zähne putzen? Jedes Bitten und Flehen sind vergebens?
Für viele Eltern von kleinen Kindern ist es ein täglicher K(r)ampf im Bad. Ein ewiges Theater und langes Diskutieren. Niemand möchte sein Kind zwingen, schon gar nicht körperlich. Aber ohne Zähneputzen keine gesunden und schönen Zähne. Was also tun?
Nicht verzweifeln! Alle geplagten Eltern von Zwei- bis Fünfjährigen finden in diesem Büchlein 21 kurze und praktische Tipps, wie sie ihr Kind zum Zähneputzen animieren können. So wird das Zähneputzen ein fester Bestandteil der Morgen- und Abendroutine. Mit Spaß und Freude und ohne Graus. Probieren Sie die Tipps heute noch aus!

```html
<!DOCTYPE html>
<html lang="de">
<head>
<meta charset="utf-8">
<title>Kleine Helden im Badezimmer – Cover</title>
<link rel="stylesheet" href="https://fonts.googleapis.com/css2?family=Bebas+Neue&family=Barlow:wght@500;600&family=Roboto+Condensed:wght@400&family=Noto+Serif:wght@700&family=Allura&display=swap">
<style>
  :root {
    --stage: #e9e9ea;
    --paper: #f1f1f2;
    --ink: #1d1d1f;
    --purple: #5a4fa2;
    --blue: #6fa6dc;
    --photo-light: #efe8ea;
    --photo-warm: #e3c6a8;
    --photo-pink: #efc9d8;
  }
  * { box-sizing: border-box; margin: 0; padding: 0; }
  html, body { width: 1200px; height: 1195px; overflow: hidden; background: var(--stage); }
  .stage { position: relative; width: 1200px; height: 1195px; }

  .cover {
    position: absolute; top: 200px; width: 540px; height: 790px;
    background: var(--paper); overflow: hidden;
    box-shadow: 0 6px 24px rgba(0,0,0,.12);
  }
  .cover--front { left: 40px; }
  .cover--back { left: 620px; }

  .author {
    position: absolute; top: 40px; left: 0; right: 0; text-align: center;
    font-family: "Roboto Condensed", sans-serif; font-size: 19px; color: var(--ink);
  }
  .title {
    position: absolute; top: 84px; left: 0; right: 0; text-align: center;
    font-family: "Bebas Neue", sans-serif; font-weight: 400; line-height: .86;
  }
  .title__line { display: block; }
  .title__line--first { color: var(--purple); font-size: 70px; }
  .title__line--second { color: var(--blue); font-size: 78px; }

  .cover-photo {
    position: absolute; left: 0; right: 0; top: 232px; bottom: 0;
    background:
      radial-gradient(ellipse 38% 30% at 32% 38%, var(--photo-warm), transparent 70%),
      radial-gradient(ellipse 40% 34% at 68% 30%, var(--photo-warm), transparent 70%),
      radial-gradient(ellipse 70% 35% at 50% 95%, var(--photo-pink), transparent 75%),
      linear-gradient(180deg, var(--photo-light) 0%, #ead7cf 55%, var(--photo-pink) 100%);
  }

  .tips-badge {
    position: absolute; left: 100px; top: 625px; width: 144px; height: 144px;
    border-radius: 50%; background: var(--purple); color: #fff;
    display: flex; flex-direction: column; align-items: center; justify-content: center;
    font-family: "Noto Serif", serif; font-weight: 700; line-height: 1;
  }
  .tips-badge__count { font-size: 46px; }
  .tips-badge__label { font-size: 20px; font-weight: 700; margin-top: 4px; }
  .tips-badge__word { font-size: 28px; margin-top: 4px; letter-spacing: .5px; }

  .audience-band {
    position: absolute; left: 238px; top: 660px; width: 210px; height: 70px;
    background: var(--blue);
    display: flex; align-items: center; justify-content: center;
    font-family: "Allura", cursive; font-size: 50px; color: #fff;
  }

  .blurb {
    position: absolute; top: 80px; left: 50px; right: 50px; text-align: center;
  }
  .blurb__lead, .blurb__call {
    font-family: "Barlow", sans-serif; font-weight: 600; color: var(--blue);
    font-size: 18px; letter-spacing: 1px; line-height: 1.3;
  }
  .blurb__text {
    font-family: "Roboto Condensed", sans-serif; font-size: 14.5px; color: var(--ink);
    line-height: 1.15; margin-top: 24px;
  }
  .blurb__accent {
    font-family: "Allura", cursive; font-size: 50px; color: var(--purple);
    margin: 22px 0 14px; line-height: 1;
  }
  .blurb__call { margin-top: 34px; }
</style>
</head>
<body>
<main class="stage">

  <section class="cover cover--front" aria-label="Vorderseite">
    <div class="cover-photo" role="img" aria-label="Foto: lachende Mutter und kleine Tochter im rosa Bademantel beim Zähneputzen"></div>
    <p class="author">Frieda Wolkenstein</p>
    <h1 class="title">
      <span class="title__line title__line--first">KLEINE HELDEN</span>
      <span class="title__line title__line--second">IM BADEZIMMER</span>
    </h1>
    <div class="audience-band">für Eltern</div>
    <div class="tips-badge">
      <span class="tips-badge__count">21</span>
      <span class="tips-badge__label">praktische</span>
      <span class="tips-badge__word">TIPPS</span>
    </div>
  </section>

  <section class="cover cover--back" aria-label="Rückseite">
    <div class="blurb">
      <p class="blurb__lead">Ihr Kind will sich partout nicht die Zähne putzen? Jedes Bitten und Flehen ist vergebens?</p>
      <p class="blurb__text">Für viele Eltern von kleinen Kindern ist es ein täglicher K(r)ampf im Bad. Ein ewiges Theater und langes Diskutieren. Niemand möchte sein Kind zwingen, schon gar nicht körperlich. Aber ohne Zähneputzen keine gesunden und schönen Zähne. Was also tun?</p>
      <p class="blurb__accent">Nicht verzweifeln!</p>
      <p class="blurb__text" style="margin-top:0">Alle geplagten Eltern von Zwei- bis Fünfjährigen finden in diesem Büchlein 21 kurze und praktische Tipps, wie sie Ihr Kind zum Zähneputzen animieren können. So wird das Zähneputzen ein fester Bestandteil der Morgen- und Abendroutine. Mit Spaß und Freude und ohne Graus.</p>
      <p class="blurb__call">Probieren Sie die Tipps<br>heute noch aus!</p>
    </div>
  </section>

</main>
</body>
</html>
```